New Business Card Design Project

Details for my new Business Card Design Project will be added soon. Like a nice simple design

Target Market(s)

Home improvement

Industry/Entity Type

Home Improvement

Contact Information for Business Card

Roofing siding gutters additions garages decks

Requirements
Must have
• Phone 5097362418
• Email korvandpm@mailnest.net

```html
<!DOCTYPE html>
<html lang="en">
<head>
<meta charset="utf-8">
<title>Handyman Services – Business Card</title>
<link href="https://fonts.googleapis.com/css2?family=PT+Sans:wght@700&family=Source+Sans+3:wght@400&family=Arimo:wght@700&display=swap" rel="stylesheet">
<style>
  :root {
    --paper: #ffffff;
    --frame-red: #e3262d;
    --title-red: #f0262f;
    --brand-blue: #0a2ed1;
    --band-sky: #4fd2f7;
    --marker-cyan: #30ebf4;
    --contact-blue: #0a1fe0;
    --white: #ffffff;
  }
  html, body {
    margin: 0;
    padding: 0;
    width: 1200px;
    height: 720px;
    overflow: hidden;
    background: var(--paper);
  }
  .business-card {
    display: block;
    width: 1200px;
    height: 720px;
  }
  .card-frame { fill: var(--paper); stroke: var(--frame-red); stroke-width: 2; }
  .brand-square { fill: var(--brand-blue); }
  .service-band { fill: var(--band-sky); }
  .band-underline { fill: var(--brand-blue); }
  .brand-title {
    font-family: "PT Sans", "Arial Narrow", sans-serif;
    font-weight: 700;
    font-size: 64px;
    fill: var(--title-red);
  }
  .service-list {
    font-family: "Source Sans 3", "Myriad Pro", sans-serif;
    font-weight: 400;
    font-size: 40px;
    fill: var(--white);
  }
  .contact-marker { fill: var(--marker-cyan); }
  .contact-leader { stroke: var(--frame-red); stroke-width: 2; }
  .marker-glyph { fill: var(--white); }
  .marker-glyph-line { fill: none; stroke: var(--marker-cyan); stroke-width: 1.4; }
  .contact-text {
    font-family: "Arimo", Arial, sans-serif;
    font-weight: 700;
    font-size: 42px;
    fill: var(--contact-blue);
  }
</style>
</head>
<body>
<svg class="business-card" viewBox="0 0 1064 638" width="1200" height="720" xmlns="http://www.w3.org/2000/svg">
  <rect class="card-frame" x="7" y="7" width="1050" height="624"/>

  <g class="masthead">
    <polygon class="service-band" points="282,155 948,155 1040,285 372,285"/>
    <rect class="band-underline" x="370" y="285" width="670" height="10"/>
    <rect class="brand-square" x="100" y="145" width="150" height="150"/>

    <text class="brand-title" x="275" y="122" textLength="648" lengthAdjust="spacingAndGlyphs">Handyman Services</text>
    <text class="service-list" x="372" y="205" textLength="490" lengthAdjust="spacingAndGlyphs">Roofing, siding, gutters,</text>
    <text class="service-list" x="425" y="265" textLength="510" lengthAdjust="spacingAndGlyphs">additions, garages decks</text>
  </g>

  <g class="contact-row contact-phone">
    <polygon class="contact-marker" points="122,343 195,395 122,447"/>
    <path class="marker-glyph" d="M140,370 c-4,2 -6,6 -4,12 c3,10 9,18 17,21 c4,1 7,0 8,-3 l-5,-5 c-2,1 -3,2 -5,1 c-3,-3 -6,-8 -7,-12 c0,-2 1,-3 3,-4 z"/>
    <line class="contact-leader" x1="195" y1="395" x2="292" y2="395"/>
    <text class="contact-text" x="300" y="413" textLength="306" lengthAdjust="spacingAndGlyphs">509-736-2418</text>
  </g>

  <g class="contact-row contact-email">
    <polygon class="contact-marker" points="122,473 197,525 122,577"/>
    <polygon class="marker-glyph" points="131,522 148,510 165,522 165,538 131,538"/>
    <polyline class="marker-glyph-line" points="131,522 148,532 165,522"/>
    <line class="contact-leader" x1="197" y1="525" x2="292" y2="525"/>
    <text class="contact-text" x="300" y="537" textLength="488" lengthAdjust="spacingAndGlyphs">korvandpm@mailnest.net</text>
  </g>
</svg>
</body>
</html>
```